Velvet Crest Car Detailing Brochure

I would like a trifold brochure designed for my car detailing business. The background has to be full black or mostly black with some designing using only colors present in our logo.

Front page must have our logo and name, list of services, a photo and mybe our phone number but no long text.

Inside I want to present each service one by one with its description and a photo representing/showing each service. (I will provide the text below). For photos, use stock photos and I will add come of mines already too.

On the back of the brochure I want to have contact & info: phone number, opening hours, address, website, Instagram.

Outside left I want the text About us and photo/design.

I want the brochure to be neat, professional, easy to read, but at the same time not too boring.

Text:
1. About us
a. the ultimate destination for car care in Geneva. We provide personalized, detail-oriented services that bring out the best in your car. With our expert techniques and dedicated approach, we ensure that your car receives the utmost care and attention. Experience a place where passion meets precision and let us create an exceptional car care experience designed just for you.
2. Services:

DETAILING & HAND WASH

• Comprehensive exterior & interior care
• Personalisation and tailored cleaning packages
• Decontamination
• Premium products
• Attention to detail for a perfect finish

POLISHING

• Eliminates scratches, holograms
• Revives and protects paint
• Ensures lasting gloss
• Enhances paint life
• Preserves car’s value and beauty

CERAMIC TREATMENT

• Durable paint protection
• Water-repellent (hydrophobic) effect
• Easier cleaning, enhanced shine
• Long-term surface safeguarding
• Shields against environmental impacts

DRY ICE WASH

• Innovative, waterless method
• Safe for all car parts
• Deep cleans, removes odors
• Allergen-free, antibacterial
• Gentle, effective
• Advanced cleaning technology

COVERING

• Personalized vehicle styling
• More than 150 colours available
• Clean cut without using a cutter
• High-quality, durable materials
• Custom designs available

PROTECTION FILM

• Invisible, durable shield
• Self-healing technology
• 10-year warranty by QR VONT

DETAILING BOUTIQUE

• Premium brands available
• Buy on site during your visit
• Marble Harbour, Zeb Autos, DRUP Polaro
• Essential for at-home car care
• Perfect for quick touch-ups
(for these three brands you can put their logos

Target Market(s)

Our target market includes car owners of all price ranges, with a special focus on those who are passionate about their vehicles. We cater to clients who value excellent service and results, and seek to maintain their cars in pristine condition.

Industry/Entity Type

Automobile / Car detailing

Colors

Designer to choose colors to be used in the design.

Requirements
Must have
• Brand Consistency: The brochure must adhere to our brand colors and style, particularly utilizing the colors present in our logo. Trifold Layout: The design must be specifically tailored for a trifold brochure format. Legibility: Text must be easy to read against the mostly black background, with appropriate font size and style. Professional Look and Feel: The overall design must convey professionalism while being engaging and not overly complex. Photo representation: each service description should have a phot presenting it.
Should not have
• Overcrowded Design: Avoid cluttering with too much text or too many images. The layout should be clean and easy to navigate. Cartoonish Fonts or Graphics: Avoid using unprofessional or casual fonts and graphics that do not align with the upscale and professional image of our business. Distracting Backgrounds: The background should complement and not overpower the content. Stick to the theme of mostly black with design elements from our logo.

```html
<!DOCTYPE html>
<html lang="en">
<head>
<meta charset="utf-8">
<title>Velvet Crest Car Detailing – Trifold Brochure</title>
<link rel="stylesheet" href="https://fonts.googleapis.com/css2?family=Poppins:wght@400;500;600;700&family=Open+Sans:wght@400&display=swap">
<style>
  :root {
    --stage: #8f8f8f;
    --panel: #1a1a1a;
    --panel-mid: #222222;
    --ink: #ececec;
    --ink-soft: #cfcfcf;
    --pink: #d6479f;
    --violet: #8a63c9;
    --blue: #4f86d6;
    --rule: #bdbdbd;
    --brand-grad: linear-gradient(90deg, var(--pink), var(--violet) 55%, var(--blue));
  }
  * { margin: 0; padding: 0; box-sizing: border-box; }
  html, body { width: 875px; height: 1200px; overflow: hidden; }
  body {
    background: var(--stage);
    font-family: "Poppins", sans-serif;
    color: var(--ink);
    position: relative;
  }
  .side-label {
    position: absolute; left: 0; width: 875px; text-align: center;
    font-family: "Open Sans", sans-serif; font-size: 34px; color: #fff; letter-spacing: 1px;
  }
  .side-label--inside { top: 6px; }
  .side-label--outside { top: 584px; }

  .sheet {
    position: absolute; left: 72px; width: 723px; height: 515px;
    display: flex; box-shadow: 0 6px 14px rgba(0,0,0,.35);
  }
  .sheet--inside { top: 53px; }
  .sheet--outside { top: 630px; }
  .sheet::before, .sheet::after {
    content: ""; position: absolute; left: 0; right: 0; height: 6px; z-index: 2;
  }
  .sheet--inside::before { top: 0; background: linear-gradient(90deg, var(--blue), var(--violet), var(--pink)); }
  .sheet--inside::after { bottom: 0; background: linear-gradient(90deg, var(--pink), var(--violet), var(--blue)); }
  .sheet--outside::before { top: 0; background: linear-gradient(90deg, var(--pink), var(--violet), var(--blue)); }
  .sheet--outside::after { bottom: 0; background: linear-gradient(90deg, var(--blue), var(--violet), var(--pink)); }

  .panel { position: relative; width: 241px; height: 515px; background: var(--panel); overflow: hidden; }
  .panel--mid { background: var(--panel-mid); }

  .abs { position: absolute; }
  .service-title {
    position: absolute; left: 15px; font-size: 10px; font-weight: 600; letter-spacing: .6px;
    background: var(--brand-grad); -webkit-background-clip: text; background-clip: text; color: transparent;
    text-transform: uppercase;
  }
  .photo { position: absolute; left: 15px; width: 208px; height: 79px; }
  .bullets { position: absolute; left: 15px; width: 222px; list-style: none; font-size: 8.5px; line-height: 10.2px; color: var(--ink); }
  .bullets li::before { content: "• "; }

  .services-heading { position: absolute; left: 14px; top: 62px; font-size: 38px; font-weight: 700; color: #fff; letter-spacing: 1px; }

  .partner-name { position: absolute; left: 15px; font-size: 17px; font-weight: 600; color: #fff; letter-spacing: .5px; }

  .about-title {
    position: absolute; left: 16px; top: 22px; font-size: 18px; font-weight: 700; letter-spacing: .6px;
    background: var(--brand-grad); -webkit-background-clip: text; background-clip: text; color: transparent;
  }
  .about-rule { position: absolute; left: 16px; top: 48px; width: 118px; height: 1px; background: var(--rule); }
  .about-text { position: absolute; left: 16px; top: 52px; width: 216px; font-size: 10.6px; line-height: 13.6px; color: #fff; }
  .about-photo { position: absolute; left: 0; top: 200px; width: 241px; height: 315px;
    background: linear-gradient(180deg, #1a1a1a 0%, #3b3b40 25%, #5a5048 55%, #2e3442 100%); }

  .brand-mark { position: absolute; left: 50%; transform: translateX(-50%); border-radius: 50%; border: 2px solid var(--violet); }
  .brand-name { position: absolute; left: 0; width: 100%; text-align: center; color: #fff; font-weight: 400; letter-spacing: .6px; }

  .info-title {
    position: absolute; left: 0; width: 100%; text-align: center; font-weight: 600; letter-spacing: 1px;
    background: var(--brand-grad); -webkit-background-clip: text; background-clip: text; color: transparent;
  }
  .info-rule { position: absolute; left: 58px; width: 125px; height: 1px; background: var(--rule); }
  .info-text { position: absolute; left: 0; width: 100%; text-align: center; font-size: 10.6px; line-height: 13px; color: #fff; letter-spacing: .4px; }
  .info-icon { position: absolute; left: 111px; width: 19px; height: 19px; }

  .cover-photo { position: absolute; inset: 0;
    background: linear-gradient(180deg, #5c5650 0%, #3d3935 35%, #6a2a2a 55%, #2a2626 78%, #161616 100%); }
  .cover-services { position: absolute; top: 390px; font-size: 9.2px; line-height: 11px; font-weight: 500; color: #fff; list-style: none; letter-spacing: .4px; }
  .cover-services li { position: relative; padding-left: 12px; margin-bottom: 4px; }
  .cover-services li::before { content: ""; position: absolute; left: 0; top: 3px; width: 4px; height: 4px; border-radius: 50%; background: var(--pink); }
  .cover-services--left { left: 38px; }
  .cover-services--right { left: 130px; }
</style>
</head>
<body>

<div class="side-label side-label--inside">INSIDE</div>
<section class="sheet sheet--inside">
  <div class="panel">
    <h1 class="services-heading">SERVICES</h1>

    <h2 class="service-title" style="top:187px">Detailing &amp; Hand Wash</h2>
    <div class="photo" style="top:201px;background:linear-gradient(120deg,#5a4a3e,#2b2b2e 60%,#151515)" role="img" aria-label="Photo of a car being hand washed with foam"></div>
    <ul class="bullets" style="top:285px">
      <li>Comprehensive exterior &amp; interior care</li>
      <li>Personalisation and tailored cleaning packages</li>
      <li>Decontamination</li>
      <li>Premium products</li>
      <li>Attention to detail for a perfect finish</li>
    </ul>

    <h2 class="service-title" style="top:349px">Polishing</h2>
    <div class="photo" style="top:364px;background:linear-gradient(110deg,#3a3d3a,#7a1f26 55%,#a8232c)" role="img" aria-label="Photo of a red car bonnet being polished by gloved hands"></div>
    <ul class="bullets" style="top:449px">
      <li>Eliminates scratches, holograms</li>
      <li>Revives and protects paint</li>
      <li>Ensures lasting gloss</li>
      <li>Enhances paint life</li>
      <li>Preserves car’s value and beauty</li>
    </ul>
  </div>

  <div class="panel panel--mid">
    <h2 class="service-title" style="top:19px">Covering</h2>
    <div class="photo" style="top:33px;background:linear-gradient(100deg,#2a2a2a,#d8d526 40%,#3a2a2a 75%,#1e1e1e)" role="img" aria-label="Photo of two people applying yellow wrap film to a car"></div>
    <ul class="bullets" style="top:117px">
      <li>Personalized vehicle styling</li>
      <li>More than 150 colours available</li>
      <li>Clean cut without using a cutter</li>
      <li>High-quality, durable materials</li>
      <li>Custom designs available</li>
    </ul>

    <h2 class="service-title" style="top:187px">Ceramic Treatment</h2>
    <div class="photo" style="top:201px;background:linear-gradient(110deg,#e2a72e,#d49422 50%,#2a2a2a)" role="img" aria-label="Photo of a yellow car receiving a ceramic coating with a polisher"></div>
    <ul class="bullets" style="top:285px">
      <li>Durable paint protection</li>
      <li>Water-repellent (hydrophobic) effect</li>
      <li>Easier cleaning, enhanced shine</li>
      <li>Long-term surface safeguarding</li>
      <li>Shields against environmental impacts</li>
    </ul>

    <h2 class="service-title" style="top:349px">Protection Film</h2>
    <div class="photo" style="top:364px;background:linear-gradient(110deg,#1f1f1f,#6a6a6a 55%,#b5b5b5)" role="img" aria-label="Photo of hands stretching clear protection film over a car"></div>
    <ul class="bullets" style="top:449px">
      <li>Invisible, durable shield</li>
      <li>Self-healing technology</li>
      <li>10-year warranty by QR VONT</li>
    </ul>
  </div>

  <div class="panel">
    <h2 class="service-title" style="top:19px">Dry Ice Wash</h2>
    <div class="photo" style="top:32px;background:linear-gradient(100deg,#cfcfcf,#eaeaea 40%,#d9d23a 60%,#b8b8b8 85%,#9a2a2a)" role="img" aria-label="Photo of a wash mitt cleaning a foamy car"></div>
    <ul class="bullets" style="top:116px">
      <li>Innovative, waterless method</li>
      <li>Safe for all car parts</li>
      <li>Deep cleans, removes odors</li>
      <li>Allergen-free, antibacterial</li>
      <li>Gentle, effective</li>
      <li>Advanced cleaning technology</li>
    </ul>

    <h2 class="service-title" style="top:187px">Detailing Boutique</h2>
    <div class="photo" style="top:203px;background:linear-gradient(110deg,#b8905a,#d6b98c 45%,#3a4150)" role="img" aria-label="Photo of a car interior being detailed"></div>
    <ul class="bullets" style="top:287px">
      <li>Premium brands available</li>
      <li>Buy on site during your visit</li>
      <li>Marble Harbour, Zeb Autos, DRUP Polaro</li>
      <li>Essential for at-home car care</li>
      <li>Perfect for quick touch-ups</li>
    </ul>

    <div class="partner-name" style="top:360px">MARBLE HARBOUR</div>
    <div class="partner-name" style="top:394px">ZEB AUTOS</div>
    <div class="partner-name" style="top:428px">DRUP POLARO</div>
  </div>
</section>

<div class="side-label side-label--outside">OUTSIDE</div>
<section class="sheet sheet--outside">
  <div class="panel" style="background:#0e0e0e">
    <h2 class="about-title">ABOUT US</h2>
    <div class="about-rule"></div>
    <p class="about-text">the ultimate destination for car care in Geneva. We provide personalized, detail-oriented services that bring out the best in your car. With our expert techniques and dedicated approach, we ensure that your car receives the utmost care and attention. Experience a place where passion meets precision and let us create an exceptional car care experience designed just for you.</p>
    <div class="about-photo" role="img" aria-label="Photo of a customer shaking hands with a mechanic in a garage"></div>
  </div>

  <div class="panel panel--mid">
    <div class="brand-mark" style="top:26px;width:42px;height:42px"></div>
    <div class="brand-name" style="top:73px;font-size:8.6px">VELVET CREST</div>

    <h2 class="info-title" style="top:126px;font-size:12px">OPENING TIMING</h2>
    <div class="info-rule" style="top:146px"></div>
    <p class="info-text" style="top:152px">Monday to Saturday<br>9 : 00 to 6 : 00</p>

    <h2 class="info-title" style="top:214px;font-size:15px">CONTACT US</h2>
    <div class="info-rule" style="top:238px"></div>

    <svg class="info-icon" style="top:253px" viewBox="0 0 20 20" aria-hidden="true">
      <rect width="20" height="20" rx="4" fill="#fff"/>
      <path d="M6 4.5c.6-.4 1.3-.3 1.7.3l1 1.6c.3.5.2 1.1-.2 1.5l-.8.7c.6 1.3 1.6 2.3 2.9 2.9l.7-.8c.4-.4 1-.5 1.5-.2l1.6 1c.6.4.7 1.1.3 1.7l-.6.9c-.5.7-1.5 1-2.3.7-3.2-1.2-5.7-3.7-6.9-6.9-.3-.8 0-1.8.7-2.3z" fill="#1a1a1a"/>
    </svg>
    <p class="info-text" style="top:282px">+000 222 333</p>

    <svg class="info-icon" style="top:303px" viewBox="0 0 20 20" aria-hidden="true">
      <rect width="20" height="20" rx="3" fill="#fff"/>
    </svg>
    <p class="info-text" style="top:330px">@Velvet Crest</p>

    <svg class="info-icon" style="top:356px" viewBox="0 0 20 20" aria-hidden="true">
      <rect width="20" height="20" rx="4" fill="#fff"/>
      <path d="M10 3.5c-2.6 0-4.5 2-4.5 4.4 0 3.2 4.5 8.3 4.5 8.3s4.5-5.1 4.5-8.3c0-2.4-1.9-4.4-4.5-4.4z" fill="#1a1a1a"/>
      <circle cx="10" cy="8" r="1.7" fill="#fff"/>
    </svg>
    <p class="info-text" style="top:382px;line-height:10px">Lorem ipsum dolor<br>sit amet, consectetuer.</p>

    <p class="info-text" style="top:468px;letter-spacing:1px">www.velvetcrest.com</p>
  </div>

  <div class="panel">
    <div class="cover-photo" role="img" aria-label="Photo of a red classic sports car parked on a city street"></div>
    <div class="brand-mark" style="top:30px;width:54px;height:54px"></div>
    <div class="brand-name" style="top:90px;font-size:11.5px">VELVET CREST</div>
    <ul class="cover-services cover-services--left">
      <li>DETAILING &amp;<br>HAND WASH</li>
      <li>CERAMIC<br>TREATMENT</li>
      <li>DETAILING<br>BOUTIQUE</li>
      <li>COVERING</li>
    </ul>
    <ul class="cover-services cover-services--right">
      <li>PROTECTION<br>FILM</li>
      <li>DRY ICE<br>WASH</li>
      <li>POLISHING</li>
    </ul>
  </div>
</section>

</body>
</html>
```